Spring FWC Lawn Care Doorhanger

I need a design for a doorhanger for a lawn care business. The door hanger should focus on the following services: Complete 6 Application Fertilization & Weed Control Program, Spring or Fall Core Aeration and Overseed.
Our business focuses on quality of service.
*Special Offer: Free Grub Control Application *with completion of new 6 app program agreement

I have attached a past version that we have used.

Font styles to use
Serif
Sans Serif

Colors
0054AA
0677BA
7BADD7
CADEEF
E8F1F8
59FF00
82FF00
B8FF75
E3FFCB
F4FFEA

```html
<!DOCTYPE html>
<html lang="en">
<head>
<meta charset="utf-8">
<title>Spring Lawn Care Door Hanger</title>
<link rel="stylesheet" href="https://fonts.googleapis.com/css2?family=Poppins:wght@500;600;700;800&family=Anton&display=swap">
<style>
:root{
  --blue:#0a4ea3;
  --blue-deep:#0054aa;
  --green:#3c9a22;
  --green-bright:#4caf28;
  --green-dark:#2d7d18;
  --red:#e0141e;
  --ink:#222;
  --white:#fff;
  --page:#f1f1f1;
  --gold:#c9a13a;
}
*{box-sizing:border-box;margin:0;padding:0}
html,body{width:755px;height:1200px;overflow:hidden}
body{background:var(--page);font-family:"Poppins",sans-serif;position:relative}
.hanger{position:absolute;top:229px;width:340px;height:741px;background:var(--white);overflow:hidden;box-shadow:0 4px 14px rgba(0,0,0,.18)}
.hanger--front{left:25px}
.hanger--back{left:390px}
.abs{position:absolute}
.door-hole{position:absolute;left:107px;top:29px;width:126px;height:126px;border-radius:50%;background:#f4f4f4;box-shadow:inset 0 2px 6px rgba(0,0,0,.18);z-index:3}

/* front */
.headline-top{top:168px;left:0;width:100%;text-align:center;font-weight:800;font-size:35px;color:var(--ink);letter-spacing:.5px;line-height:1}
.headline-main{top:203px;left:0;width:100%;text-align:center;font-family:"Anton",sans-serif;font-size:47px;color:var(--blue);line-height:1;letter-spacing:.3px}
.tagline-band{top:256px;left:0;width:100%;height:43px;background:var(--green);color:var(--white);text-align:center;font-weight:700;font-size:16.5px;line-height:18.5px;padding-top:3px}
.photo{background:linear-gradient(180deg,#8fa39a 0%,#b7b56a 35%,#7fa83a 70%,#5a8d22 100%)}
.photo--mower{top:299px;left:0;width:100%;height:170px}
.member-box{top:469px;left:0;width:100%;height:85px;background:var(--white);border-top:4px solid var(--blue);border-left:6px solid var(--blue);border-bottom:5px solid var(--blue)}
.guarantee-seal{left:26px;top:18px;width:56px;height:56px;border-radius:50%;background:radial-gradient(circle,#2a2a2a 0 52%,var(--gold) 54% 100%)}
.member-label{left:98px;top:12px;font-family:"Anton",sans-serif;font-size:15px;color:var(--ink)}
.association{left:98px;top:36px;display:flex;align-items:center;gap:6px}
.association-square{width:16px;height:16px;background:var(--green)}
.association-name{font-size:7.5px;line-height:8.5px;color:#444;font-weight:600;text-transform:uppercase}
.lawn-circle{left:220px;top:457px;width:106px;height:106px;border-radius:50%;border:4px solid var(--green);background:linear-gradient(180deg,#dfeaf0 0%,#c8dbe4 40%,#3e6e2a 55%,#5c9a2c 100%)}
.brand{top:585px;left:0;width:100%;display:flex;justify-content:center;align-items:center;gap:8px}
.brand-dot{width:14px;height:14px;border-radius:50%;background:var(--green)}
.brand-name{font-weight:800;font-size:26px;color:var(--blue)}
.swoosh{left:0;top:636px;width:100%;height:50px}
.phone{top:667px;left:0;width:100%;text-align:center;font-weight:800;font-size:34px;color:var(--green-bright);line-height:1;letter-spacing:.5px}
.web{top:708px;left:0;width:100%;text-align:center;font-weight:600;font-size:15px;color:var(--ink);letter-spacing:2px}

/* back */
.grass-band{top:0;left:0;width:100%;height:41px;background:linear-gradient(180deg,#3d9a22,#2f8a18)}
.photo--spreader{top:41px;left:0;width:100%;height:149px;background:linear-gradient(90deg,#476a5a 0%,#6b7f6a 35%,#3f6a2c 60%,#6ea534 100%)}
.services{top:190px;left:0;width:100%;height:148px;background:var(--white);border-top:4px solid var(--blue);border-left:8px solid var(--blue)}
.services-title{top:16px;left:0;width:100%;text-align:center;font-weight:800;font-size:19px;line-height:1}
.services-title .dark{color:var(--ink);text-decoration:underline;text-underline-offset:3px}
.services-title .green{color:var(--green-bright)}
.service-list{top:48px;left:12px;list-style:none;width:180px}
.service-list li{display:flex;gap:6px;font-size:11px;font-weight:500;line-height:14px;color:var(--ink);margin-bottom:5px}
.tick{flex:none;width:9px;height:9px;margin-top:3px}
.services-thumb{left:210px;top:53px;width:106px;height:70px;border-radius:16px 0 16px 0;border:2px solid var(--green);background:linear-gradient(180deg,#c7dcc9 0%,#4f7e32 45%,#6db33a 100%)}
.services-rule{left:0;bottom:0;width:96%;height:3px;background:var(--blue)}
.award-band{top:338px;left:0;width:100%;height:78px;background:var(--green)}
.award-seal{left:63px;top:9px;width:62px;height:58px;border-radius:50%;background:var(--red);border:3px solid #f6d5d5}
.award-box{left:139px;top:14px;width:147px;height:48px;border:2px solid var(--white);color:var(--white);font-weight:700;font-size:17.5px;line-height:18px;padding:4px 0 0 8px;letter-spacing:.3px}
.offer-box{top:430px;left:21px;width:301px;height:144px;border:1.5px dashed var(--green)}
.offer-title{top:6px;left:0;width:100%;text-align:center;font-weight:800;font-size:31px;color:var(--red);line-height:1.1}
.offer-item{top:42px;left:0;width:100%;text-align:center;font-weight:800;font-size:22.5px;line-height:1.1}
.offer-item .blue{color:var(--blue)}
.offer-item .green{color:var(--green-bright)}
.offer-sub{top:68px;left:0;width:100%;text-align:center;font-weight:600;font-size:16px;letter-spacing:4.5px;color:var(--ink)}
.offer-terms{top:89px;left:19px;width:263px;height:41px;background:var(--blue);color:var(--white);text-align:center;font-weight:600;font-size:10.5px;line-height:13px;padding-top:3px}
.offer-terms strong{font-weight:800;font-size:13px;display:block;line-height:16px}
.quality{top:584px;left:56px;display:flex;align-items:center;gap:10px}
.quality-icon{width:52px;height:52px}
.quality-text{font-size:13px;font-weight:500;line-height:14px;color:var(--ink)}
.quality-text strong{font-weight:700}
</style>
</head>
<body>

<section class="hanger hanger--front">
  <div class="door-hole"></div>
  <h1 class="abs headline-top">WE’RE IN YOUR</h1>
  <h2 class="abs headline-main">NEIGHBORHOOD</h2>
  <p class="abs tagline-band">SPEND MORE TIME DOING<br>WHAT YOU LOVE</p>
  <div class="abs photo photo--mower" role="img" aria-label="Photo of a yellow ride-on spreader treating a front lawn"></div>
  <div class="abs member-box">
    <div class="abs guarantee-seal"></div>
    <p class="abs member-label">MEMBER OF</p>
    <div class="abs association">
      <span class="association-square"></span>
      <span class="association-name">Regional Guild<br>of Lawn Pros</span>
    </div>
  </div>
  <div class="abs lawn-circle" role="img" aria-label="Photo of a wide green lawn with trees"></div>
  <div class="abs brand"><span class="brand-dot"></span><span class="brand-name">Verdant Lawn Care</span></div>
  <svg class="abs swoosh" viewBox="0 0 340 50" preserveAspectRatio="none" aria-hidden="true">
    <path d="M0 42 Q170 -12 340 34 L340 40 Q170 -2 0 48 Z" fill="#3c9a22"/>
  </svg>
  <p class="abs phone">555-014-7290</p>
  <p class="abs web">www.verdantlawn.com</p>
</section>

<section class="hanger hanger--back">
  <div class="abs grass-band"></div>
  <div class="abs photo photo--spreader" role="img" aria-label="Photo of a green spreader spraying over a lawn beside pine trees"></div>
  <div class="door-hole"></div>
  <div class="abs services">
    <h3 class="abs services-title"><span class="dark">OUR</span> <span class="green">SERVICES</span></h3>
    <ul class="abs service-list">
      <li><svg class="tick" viewBox="0 0 10 10"><path d="M1 5 L4 8 L9 1" stroke="#3c9a22" stroke-width="2" fill="none"/></svg>Complete 6 Application Fertilization</li>
      <li><svg class="tick" viewBox="0 0 10 10"><path d="M1 5 L4 8 L9 1" stroke="#3c9a22" stroke-width="2" fill="none"/></svg>Weed Control Program</li>
      <li><svg class="tick" viewBox="0 0 10 10"><path d="M1 5 L4 8 L9 1" stroke="#3c9a22" stroke-width="2" fill="none"/></svg>Spring or Fall Core Aeration and Overseed</li>
    </ul>
    <div class="abs services-thumb" role="img" aria-label="Photo of a trimmed lawn with shrubs"></div>
    <div class="abs services-rule"></div>
  </div>
  <div class="abs award-band">
    <div class="abs award-seal"></div>
    <p class="abs award-box">FAVORITE<br>LANDSCAPER</p>
  </div>
  <div class="abs offer-box">
    <p class="abs offer-title">SPECIAL OFFER</p>
    <p class="abs offer-item"><span class="blue">FREE</span> <span class="green">GRUB CONTROL</span></p>
    <p class="abs offer-sub">APPLICATION</p>
    <p class="abs offer-terms">WITH COMPLETION OF NEW<strong>6 APP PROGRAM AGREEMENT</strong></p>
  </div>
  <div class="abs quality">
    <svg class="quality-icon" viewBox="0 0 52 52" aria-hidden="true">
      <circle cx="26" cy="26" r="25" fill="#3c9a22"/>
      <circle cx="26" cy="26" r="20" fill="none" stroke="#fff" stroke-width="1.5"/>
      <path d="M26 13 L36 17 V26 Q36 35 26 40 Q16 35 16 26 V17 Z" fill="none" stroke="#fff" stroke-width="2"/>
      <path d="M21 26 L25 30 L32 22" fill="none" stroke="#fff" stroke-width="2.4"/>
    </svg>
    <p class="quality-text">Our business focuses on<br><strong>QUALITY OF SERVICE</strong></p>
  </div>
  <svg class="abs swoosh" viewBox="0 0 340 50" preserveAspectRatio="none" aria-hidden="true">
    <path d="M0 42 Q170 -12 340 34 L340 40 Q170 -2 0 48 Z" fill="#3c9a22"/>
  </svg>
  <p class="abs phone">555-014-7290</p>
  <p class="abs web">www.verdantlawn.com</p>
</section>

</body>
</html>
```